CEO of company needs clear business card that stands out from the rest

I need a clear business card (standard credit card size) for the CEO/Founder of our company...Brightfield Counseling. We would like to see designs that use our logo colors, which are khaki, chocolate brown, and gray. The card should be an edgy design, maybe where half the card is transparent with curves on the card, or a textured card where the logo is transparent, I don't care much for white cards. The final design should communicate a funky, edgy, and modern look, as well as stand out to have the "WOW" factor. The information we need on the card would be Name, Title, Toll free number, Phone Number, address, email address, and website.

*PLEASE SEND FRONT AND BACK OF CARDS

Card is two sided front and back please give us your front and back designs

The card should be an edgy design, maybe where half the card is transparent with curves on the card, or a textured card where the logo is transparent, I don't care much for white cards. The final design should communicate a funky, edgy, and modern look, as well as stand out to have the "WOW" factor.

Please follow these guidelines for the card

SPECS (card):

2.125 (h) x 3.375 (w) card size after cut

2.375 (h) x 3.625 (w) card with bleed

300 dpi

cmyk

1/8 bleed

allow 1/8 border for live area

I will also attached the pdf for the information listed above which includes a diagram of the card

 

All the cards need to have rounded edges

I just updated a card as an example of how you can use different fonts on a single business card, look how the name is written in script, so what I am saying is make this a card you will be proud to design and put it in your portfolio 

Reason: this race is really close and I am working with 2 designers to fine tune their designs and the weekend is slowing us down

• Our Logo
MUST HAVE PARTS OF CARD THAT ARE TRANSPARENT. See ideas that are attached.
Card is two sided front and back
• The final design should communicate a funky, edgy, and modern look, as well as stand out to have the "WOW" factor. The information we need on the card would be Name, Title, Toll free number, Phone Number, address, email address, and website.

```html
<!DOCTYPE html>
<html lang="en">
<head>
<meta charset="utf-8">
<title>Brightfield Counseling – Founder Business Card</title>
<link rel="stylesheet" href="https://fonts.googleapis.com/css2?family=Arimo:wght@400;700&display=swap">
<style>
  :root {
    --backdrop: #e4ddd3;
    --card-light: #efefe9;
    --chocolate: #7b4a2b;
    --chocolate-deep: #5e3820;
    --chocolate-soft: #8a5634;
    --khaki: #b9a591;
    --gray-light: #dcdcd8;
    --gray: #b4b4b0;
    --ink: #1e1e1e;
    --line-light: #d8cfc6;
    --white: #ffffff;
  }
  * { box-sizing: border-box; margin: 0; padding: 0; }
  html, body { width: 1175px; height: 1200px; overflow: hidden; }
  body {
    background: var(--backdrop);
    font-family: "Arimo", Arial, sans-serif;
    position: relative;
  }
  .card {
    position: absolute;
    left: 157px;
    width: 860px;
    height: 541px;
    border-radius: 8px;
    overflow: hidden;
  }
  .card--front { top: 40px; background: var(--card-light); }
  .card--back { top: 619px; background: var(--chocolate); }

  /* Large decorative cut-out area (placeholder) */
  .cutout {
    position: absolute;
    border-radius: 46% 46% 50% 50% / 40% 40% 60% 60%;
  }
  .card--front .cutout {
    left: 24px; top: 30px; width: 370px; height: 460px;
    background: radial-gradient(ellipse at 50% 45%, var(--card-light) 0%, var(--gray-light) 65%, var(--gray) 100%);
  }
  .card--back .cutout {
    left: 462px; top: 24px; width: 370px; height: 480px;
    background: radial-gradient(ellipse at 50% 50%, var(--chocolate-soft) 0%, var(--chocolate) 60%, var(--chocolate-deep) 100%);
  }

  /* Brand mark (name only) */
  .brand {
    position: absolute;
    display: flex;
    align-items: center;
    gap: 8px;
    font-weight: 700;
    font-size: 18px;
    letter-spacing: 0.2px;
    white-space: nowrap;
  }
  .brand__dot { width: 14px; height: 14px; border-radius: 50%; flex: none; }
  .card--front .brand { left: 110px; top: 250px; color: var(--chocolate); }
  .card--front .brand__dot { background: var(--chocolate); }
  .card--back .brand { left: 560px; top: 250px; color: var(--white); }
  .card--back .brand__dot { background: var(--white); }

  /* Front details */
  .details { position: absolute; left: 420px; top: 160px; width: 400px; }
  .details__title {
    font-size: 20px; color: var(--ink); letter-spacing: 0.5px;
    padding-left: 106px; margin-bottom: 12px;
  }
  .details__name-band {
    display: flex; align-items: center; gap: 16px;
    background: var(--khaki);
    height: 48px; padding-left: 16px;
    color: var(--white); font-size: 25px; letter-spacing: 1px;
    margin-bottom: 20px;
  }
  .details__row {
    display: flex; align-items: center; gap: 14px;
    font-size: 19px; color: var(--ink); letter-spacing: 0.4px;
    height: 48px;
  }
  .details__row svg { width: 22px; height: 22px; flex: none; fill: var(--chocolate); }
  .details__web {
    display: inline-block; margin-top: 6px;
    font-size: 19px; color: var(--ink); letter-spacing: 0.4px;
    padding: 8px 0;
    border-top: 2px solid var(--khaki);
    border-bottom: 2px solid var(--khaki);
  }

  /* Back */
  .back__rule { position: absolute; width: 3px; background: var(--line-light); }
  .back__rule--upper { left: 122px; top: 0; height: 250px; }
  .back__rule--lower { left: 375px; top: 318px; height: 180px; }
  .back__web {
    position: absolute; left: 118px; top: 280px;
    font-size: 22px; letter-spacing: 1.5px; color: var(--ink); white-space: nowrap;
  }
  .back__web-name { color: var(--khaki); }
</style>
</head>
<body>

<section class="card card--front" aria-label="Business card front">
  <div class="cutout" role="img" aria-label="Large gray cut-out decorative shape"></div>
  <div class="brand"><span class="brand__dot"></span>Brightfield Counseling</div>

  <div class="details">
    <p class="details__title">THE FOUNDER</p>
    <div class="details__name-band">
      <svg width="22" height="22" viewBox="0 0 24 24" fill="#ffffff" aria-hidden="true"><circle cx="12" cy="7" r="5"/><path d="M2 23c0-6 4.5-9 10-9s10 3 10 9z"/></svg>
      MARTIN LEWIS OAKES
    </div>
    <p class="details__row">
      <svg viewBox="0 0 24 24" aria-hidden="true"><path d="M6 1h12a2 2 0 0 1 2 2v18a2 2 0 0 1-2 2H6a2 2 0 0 1-2-2V3a2 2 0 0 1 2-2zm1 3v6h10V4zm0 9v2h2v-2zm4 0v2h2v-2zm4 0v2h2v-2zm-8 4v2h2v-2zm4 0v2h2v-2zm4 0v2h2v-2z"/></svg>
      015420736200
    </p>
    <p class="details__row">
      <svg viewBox="0 0 24 24" aria-hidden="true"><path d="M12 2 1 12h3v10h6v-6h4v6h6V12h3z"/></svg>
      28 LINDEN STREET IN MADRID
    </p>
    <p class="details__row">
      <svg viewBox="0 0 24 24" aria-hidden="true"><path d="M1 4h22v16H1zm2 2v.5l9 6.5 9-6.5V6zm0 3v9h18V9l-9 6.5z"/></svg>
      MARTIN@MAILBOX.COM
    </p>
    <p class="details__web">WWW.BRIGHTFIELDSITE.COM</p>
  </div>
</section>

<section class="card card--back" aria-label="Business card back">
  <span class="back__rule back__rule--upper"></span>
  <span class="back__rule back__rule--lower"></span>
  <p class="back__web">WWW.<span class="back__web-name">BRIGHTFIELD</span>.COM</p>
  <div class="cutout" role="img" aria-label="Large chocolate cut-out decorative shape"></div>
  <div class="brand"><span class="brand__dot"></span>Brightfield Counseling</div>
</section>

</body>
</html>
```